UNIQUE, Elegant business card for transport company.

MUST BE AN ACTUAL GRAPHIC DESIGNER.
NO TEMPLATES, NO MOCKUP GENERATORS.
Looking for a top notch, head turning, business card.
Will be printed on premium luxury paper with spot glossing and debossing.
Must know how to set up for spot glossing. Must be willing to work on the file to meet printers spec after final design.

Target Market(s)

All info on .psd file

Contact Information for Business Card

All info on .psd file

Requirements
Must have
• All info on .psd file
Nice to have
• All info on .psd file
Should not have
• Nothing red

```html
<!DOCTYPE html>
<html lang="en">
<head>
<meta charset="utf-8">
<title>Veltra Transport, Inc. — Business Card</title>
<link rel="stylesheet" href="https://fonts.googleapis.com/css2?family=Oswald:wght@600&family=Montserrat:wght@300;400&family=Archivo+Black&family=Cinzel:wght@700&display=swap">
<style>
  :root {
    --page: #2b2b2d;
    --ink-dark: #141416;
    --ink-dark-2: #2a2a2d;
    --silver: #b9bcc1;
    --silver-soft: #8e9196;
    --blue: #2a7cb8;
    --blue-deep: #1f6aa6;
    --blue-light: #8fcbed;
    --white: #ffffff;
  }
  * { box-sizing: border-box; margin: 0; padding: 0; }
  html, body { width: 1200px; height: 881px; overflow: hidden; }
  body {
    background: var(--page);
    position: relative;
    font-family: "Montserrat", sans-serif;
  }
  .card {
    position: absolute;
    left: 290px;
    width: 620px;
    height: 354px;
    border-radius: 18px;
    overflow: hidden;
    box-shadow: 0 10px 30px rgba(0,0,0,.45);
  }

  /* ---------- back card ---------- */
  .card-back {
    top: 56px;
    background: linear-gradient(135deg, var(--ink-dark-2) 0%, var(--ink-dark) 60%, #1c1c1f 100%);
    color: var(--silver);
  }
  .tagline {
    position: absolute;
    left: 36px; right: 36px; top: 32px;
    font-family: "Oswald", sans-serif;
    font-weight: 600;
    font-size: 33px;
    line-height: 1.2;
    letter-spacing: .5px;
    text-transform: uppercase;
    text-align: center;
    white-space: nowrap;
    color: var(--silver);
  }
  .credentials {
    position: absolute;
    left: 36px; right: 36px; top: 84px;
    display: flex; align-items: center; gap: 12px;
    font-weight: 300;
    font-size: 15px;
    letter-spacing: 1px;
    white-space: nowrap;
    color: var(--silver);
  }
  .credentials::before,
  .credentials::after {
    content: "";
    flex: 1;
    height: 1px;
    background: var(--silver-soft);
  }
  .brand-mark {
    position: absolute;
    left: 50%; top: 176px;
    transform: translateX(-50%);
    display: flex; align-items: center; gap: 10px;
    font-weight: 400;
    font-size: 26px;
    letter-spacing: 4px;
    color: var(--blue-light);
  }
  .brand-mark .dot {
    width: 18px; height: 18px; border-radius: 50%;
    background: var(--blue);
  }
  .back-contact {
    position: absolute;
    bottom: 30px;
    font-weight: 300;
    font-size: 15px;
    line-height: 1.45;
    letter-spacing: 1px;
    color: var(--silver);
  }
  .back-contact.left { left: 36px; }
  .back-contact.right { right: 36px; text-align: right; }

  /* ---------- front card ---------- */
  .card-front {
    top: 470px;
    background: var(--white);
  }
  .front-band {
    position: absolute; inset: 0;
    width: 100%; height: 100%;
  }
  .company {
    position: absolute;
    left: 34px; right: 34px; top: 32px;
    font-family: "Archivo Black", sans-serif;
    font-size: 29px;
    letter-spacing: 2px;
    white-space: nowrap;
    color: var(--blue);
  }
  .front-mark {
    position: absolute;
    left: 50%; top: 100px;
    transform: translateX(-50%);
    display: flex; align-items: center; gap: 10px;
    font-weight: 400;
    font-size: 24px;
    letter-spacing: 4px;
    color: var(--blue-deep);
  }
  .front-mark .dot {
    width: 16px; height: 16px; border-radius: 50%;
    background: var(--blue);
  }
  .person {
    position: absolute;
    left: 40px; bottom: 40px;
    color: var(--white);
  }
  .person-name {
    font-family: "Cinzel", serif;
    font-weight: 700;
    font-size: 30px;
    letter-spacing: 2px;
  }
  .person-role {
    font-weight: 400;
    font-size: 20px;
    letter-spacing: 1px;
  }
  .front-contact {
    position: absolute;
    right: 34px; top: 178px;
    list-style: none;
    color: var(--white);
    font-size: 15px;
    line-height: 1.5;
    letter-spacing: .5px;
    text-align: right;
  }
  .front-contact li { display: flex; justify-content: flex-end; align-items: center; gap: 8px; }
  .front-contact svg { width: 13px; height: 13px; flex: none; }
</style>
</head>
<body>

  <section class="card card-back" aria-label="Business card back">
    <div class="tagline">Every mile handled with real care</div>
    <div class="credentials">Licensed. Bonded. &amp; Insured.</div>
    <div class="brand-mark"><span class="dot"></span>VELTRA</div>
    <div class="back-contact left">(555) BOOK VLT<br>US DOT 7281046</div>
    <div class="back-contact right">(555) 266-0193<br>MC # 4820317</div>
  </section>

  <section class="card card-front" aria-label="Business card front">
    <svg class="front-band" viewBox="0 0 620 354" preserveAspectRatio="none" aria-hidden="true">
      <defs>
        <linearGradient id="bandGradient" x1="0" y1="0" x2="1" y2="0">
          <stop offset="0" stop-color="#2a7cb8"/>
          <stop offset=".5" stop-color="#8fcbed"/>
          <stop offset="1" stop-color="#2a7cb8"/>
        </linearGradient>
      </defs>
      <path d="M0 232 L270 190 L270 160 L620 110 L620 354 L0 354 Z" fill="url(#bandGradient)"/>
    </svg>
    <div class="company">VELTRA TRANSPORT, INC.</div>
    <div class="front-mark"><span class="dot"></span>VELTRA</div>
    <div class="person">
      <div class="person-name">NOEL CARTER</div>
      <div class="person-role">Transporter</div>
    </div>
    <ul class="front-contact">
      <li>(555) 624-1837
        <svg viewBox="0 0 24 24" fill="none" stroke="currentColor" stroke-width="2"><path d="M5 3h4l2 5-3 2a12 12 0 0 0 6 6l2-3 5 2v4a2 2 0 0 1-2 2A17 17 0 0 1 3 5a2 2 0 0 1 2-2z"/></svg></li>
      <li>(555) 913-2750
        <svg viewBox="0 0 24 24" fill="none" stroke="currentColor" stroke-width="2"><rect x="7" y="2" width="10" height="20" rx="2"/><line x1="11" y1="18" x2="13" y2="18"/></svg></li>
      <li>noel@veltratransport.com
        <svg viewBox="0 0 24 24" fill="none" stroke="currentColor" stroke-width="2"><rect x="3" y="5" width="18" height="14" rx="1"/><path d="M3 6l9 7 9-7"/></svg></li>
      <li>www.veltratransport.com
        <svg viewBox="0 0 24 24" fill="none" stroke="currentColor" stroke-width="2"><circle cx="12" cy="12" r="9"/><path d="M3 12h18M12 3c3 3 3 15 0 18M12 3c-3 3-3 15 0 18"/></svg></li>
    </ul>
  </section>

</body>
</html>
```